Dynamic Business Card for Sports Supplements Company

Hi! I'm looking for an awesome business card to match my existing sports supplement company. I have uploaded my current company logo and screenshot of the front page of my website.

I would like to have something dynamic and interesting and utilize the colors in the website - the reds and purples

The business card should be double sided and focus on a unique eye-catching design on the back and include all the relevant company info.

Most importantly, it should say somewhere: "Sign up on our website for a coupon code."

Target Market(s)

Mostly for women gym goers but it shouldn't be too feminine. It should be in keeping with the website design. It should flow and clearly be connected to it

Industry/Entity Type

Business

Contact Information for Business Card

Lorena K. Vasquez
CEO
LVasquez@Fortivanco.example
www.fortivanco.example
614.275.3081
P.O. Box 48317
Alder Falls, Ohio 22417

Sign up on our website for a coupon code

Font styles to use
Serif
Sans Serif
Other font styles liked:
• Novecento font family and "Fortivan" is in AR Destine font

Requirements
Must have
• One side should be a bold Fortivan logo design. Even just the symbol itself may be o.k. (see attached file)

```html
<!DOCTYPE html>
<html lang="en">
<head>
<meta charset="utf-8">
<title>Fortivan Business Card</title>
<link href="https://fonts.googleapis.com/css2?family=Roboto:wght@300;400;900&display=swap" rel="stylesheet">
<style>
  :root {
    --stage: #e9e6e2;
    --card-black: #111112;
    --card-black-soft: #262628;
    --brand-red: #e8192c;
    --brand-red-light: #f2424f;
    --white: #ffffff;
    --muted: #c9c9cb;
    --rule: #6b6b6e;
  }
  * { box-sizing: border-box; margin: 0; padding: 0; }
  html, body {
    width: 1200px; height: 950px; overflow: hidden;
    background: var(--stage);
    font-family: "Roboto", Arial, sans-serif;
  }
  .canvas { position: relative; width: 1200px; height: 950px; }
  .card {
    position: absolute; left: 250px; width: 700px; height: 400px;
    border-radius: 4px; overflow: hidden;
    box-shadow: 0 12px 28px rgba(0,0,0,.25);
  }
  .card--front { top: 50px; background: linear-gradient(135deg, var(--card-black-soft), var(--card-black) 60%); color: var(--white); }
  .card--back { top: 500px; background: linear-gradient(120deg, var(--brand-red) 45%, var(--brand-red-light)); color: var(--white); }

  .front-decor { position: absolute; left: 0; top: 0; width: 420px; height: 400px; }

  .wordmark { display: flex; align-items: center; gap: 12px; }
  .wordmark__mark { width: 22px; height: 22px; background: var(--brand-red); }
  .card--back .wordmark__mark { background: var(--white); }
  .wordmark__name { font-weight: 900; font-size: 44px; letter-spacing: 1px; text-transform: uppercase; color: var(--white); line-height: 1; }
  .tagline { font-weight: 300; font-size: 11px; letter-spacing: 3.2px; text-transform: uppercase; color: var(--muted); margin-top: 8px; }
  .card--back .tagline { color: var(--white); }

  .front-brand { position: absolute; right: 56px; top: 60px; text-align: right; }
  .front-brand .wordmark { justify-content: flex-end; }
  .front-rule { position: absolute; right: 56px; top: 168px; width: 300px; height: 1px; background: var(--rule); }
  .address { position: absolute; right: 56px; top: 192px; text-align: right; font-style: normal; font-weight: 300; font-size: 16px; line-height: 1.6; }

  .person { position: absolute; left: 50px; bottom: 50px; }
  .person__name { color: var(--brand-red); font-weight: 400; font-size: 26px; }
  .person__role { font-weight: 300; font-size: 14px; margin: 4px 0 16px; }
  .contact { list-style: none; font-weight: 300; font-size: 15px; line-height: 1.75; }
  .contact li { display: flex; align-items: center; gap: 10px; }
  .contact svg { width: 14px; height: 14px; fill: var(--brand-red); }

  .back-brand { position: absolute; left: 0; right: 0; top: 130px; display: flex; flex-direction: column; align-items: center; }
  .back-brand .wordmark__name { font-size: 58px; }
  .offer { margin-top: 26px; font-weight: 300; font-size: 16px; letter-spacing: .5px; }
</style>
</head>
<body>
<div class="canvas">

  <section class="card card--front" aria-label="Card front">
    <svg class="front-decor" viewBox="0 0 420 400" role="img" aria-label="Faint diagonal brand decoration">
      <defs>
        <linearGradient id="decorFade" x1="0" y1="0" x2="1" y2="1">
          <stop offset="0" stop-color="#8a1a22" stop-opacity=".35"/>
          <stop offset="1" stop-color="#3a3a3d" stop-opacity=".15"/>
        </linearGradient>
      </defs>
      <polygon points="0,40 260,40 420,260 420,400 0,400" fill="url(#decorFade)"/>
    </svg>

    <div class="front-brand">
      <div class="wordmark"><span class="wordmark__mark"></span><span class="wordmark__name">Fortivan</span></div>
      <div class="tagline">Built for your best</div>
    </div>
    <div class="front-rule"></div>
    <address class="address">P.O. Box 48317<br>Alder Falls, Ohio 22417</address>

    <div class="person">
      <div class="person__name">Lorena K. Vasquez</div>
      <div class="person__role">CEO</div>
      <ul class="contact">
        <li><svg viewBox="0 0 16 16"><path d="M3 1h3l1.5 4-2 1.3a9 9 0 0 0 4.2 4.2L11 8.5l4 1.5v3a2 2 0 0 1-2 2A12 12 0 0 1 1 3a2 2 0 0 1 2-2z"/></svg>614.275.3081</li>
        <li><svg viewBox="0 0 16 16"><path d="M1 3h14v10H1z M1 3l7 6 7-6" stroke="#111" stroke-width="1"/></svg>LVasquez@Fortivanco.example</li>
        <li><svg viewBox="0 0 16 16"><circle cx="8" cy="8" r="7"/></svg>www.fortivanco.example</li>
      </ul>
    </div>
  </section>

  <section class="card card--back" aria-label="Card back">
    <div class="back-brand">
      <div class="wordmark"><span class="wordmark__mark"></span><span class="wordmark__name">Fortivan</span></div>
      <div class="tagline">Built for your best</div>
      <p class="offer">Sign up on our website for a coupon code</p>
    </div>
  </section>

</div>
</body>
</html>
```